Album/CD cover art for album named Hollow Lanterns, by the band Velvet Meridian

I would like an album cover. The album will have a wreath of flowers similar to the first file download. In two of the flowers (white large) will the drawn faces of the two pictures attached. The bird flying out of the wreath will be a Falcon.

```html
<!DOCTYPE html>
<html lang="en">
<head>
<meta charset="utf-8">
<title>Hollow Lanterns — Velvet Meridian</title>
<link rel="stylesheet" href="https://fonts.googleapis.com/css2?family=Londrina+Solid:wght@300;400&display=swap">
<style>
  :root {
    --cover-bg: #18171c;
    --blush: #f7c6c2;
    --white: #ffffff;
    --wreath-pink: #e67f98;
    --wreath-rose: #f2a7b6;
    --wreath-violet: #9468ad;
    --wreath-green: #86a25e;
    --wreath-yellow: #d8d069;
    --petal-white: #f4f2ee;
    --falcon-brown: #7d5f45;
    --falcon-light: #d6c2a6;
    --stars: #cfc9dc;
  }
  * { margin: 0; padding: 0; box-sizing: border-box; }
  html, body {
    width: 1200px; height: 1200px; overflow: hidden;
    background: var(--cover-bg);
  }
  .cover {
    position: relative;
    width: 1200px; height: 1200px;
    background: var(--cover-bg);
    font-family: "Londrina Solid", "Arial Narrow", sans-serif;
    font-weight: 300;
    text-transform: uppercase;
    overflow: hidden;
  }
  .artwork { position: absolute; inset: 0; width: 1200px; height: 1200px; }
  .credits {
    position: absolute; left: 66px; top: 40px;
    line-height: 58px; letter-spacing: 2px; font-size: 42px;
  }
  .credits span { display: block; }
  .credits .artist { color: var(--blush); }
  .credits .title { color: var(--white); }
  .catalogue {
    position: absolute; left: 62px; top: 1032px;
    color: var(--white); font-size: 66px; font-weight: 400;
    letter-spacing: 3px; line-height: 1;
  }
  .series {
    position: absolute; left: 64px; top: 1112px;
    color: var(--blush); font-size: 30px;
    letter-spacing: 2px; line-height: 1;
  }
  .label-mark {
    position: absolute; left: 932px; top: 959px;
    width: 190px; height: 190px; border-radius: 50%;
    border: 3px solid var(--white);
    display: flex; align-items: center; justify-content: center;
    color: var(--white); font-size: 36px; letter-spacing: 2px;
  }
</style>
</head>
<body>
<main class="cover">
  <svg class="artwork" viewBox="0 0 1200 1200" xmlns="http://www.w3.org/2000/svg">
    <defs>
      <linearGradient id="starBand" x1="0" y1="0" x2="0" y2="1">
        <stop offset="0" stop-color="var(--stars)" stop-opacity="0"/>
        <stop offset="0.5" stop-color="var(--stars)" stop-opacity="0.18"/>
        <stop offset="1" stop-color="var(--stars)" stop-opacity="0"/>
      </linearGradient>
      <linearGradient id="wreathTone" x1="0" y1="0" x2="1" y2="1">
        <stop offset="0" stop-color="var(--wreath-rose)"/>
        <stop offset="0.3" stop-color="var(--wreath-violet)"/>
        <stop offset="0.55" stop-color="var(--wreath-pink)"/>
        <stop offset="0.8" stop-color="var(--wreath-yellow)"/>
        <stop offset="1" stop-color="var(--wreath-green)"/>
      </linearGradient>
      <radialGradient id="petalTone">
        <stop offset="0.55" stop-color="var(--petal-white)"/>
        <stop offset="1" stop-color="var(--petal-white)" stop-opacity="0.75"/>
      </radialGradient>
      <radialGradient id="falconTone">
        <stop offset="0" stop-color="var(--falcon-light)" stop-opacity="0.9"/>
        <stop offset="0.7" stop-color="var(--falcon-brown)" stop-opacity="0.7"/>
        <stop offset="1" stop-color="var(--falcon-brown)" stop-opacity="0"/>
      </radialGradient>
    </defs>

    <rect class="star-band" x="0" y="528" width="1200" height="116" fill="url(#starBand)"
          role="img" aria-label="Horizontal band of scattered tiny white stars"/>

    <path class="flower-wreath" role="img"
          aria-label="Round wreath of pink lilies, violet blooms, yellow protea, berries and green leaves"
          fill="url(#wreathTone)" fill-rule="evenodd"
          d="M570 172 A424 424 0 1 1 569.9 172 Z M570 386 A210 210 0 1 0 570.1 386 Z"/>

    <circle class="portrait-flower" cx="322" cy="372" r="92" fill="url(#petalTone)"
            role="img" aria-label="Large white flower holding a drawn portrait of the first band member"/>
    <circle class="portrait-flower" cx="848" cy="862" r="84" fill="url(#petalTone)"
            role="img" aria-label="Large white flower holding a drawn portrait of the second band member"/>

    <ellipse class="falcon falcon-top" cx="900" cy="240" rx="215" ry="150" fill="url(#falconTone)"
             role="img" aria-label="Falcon with spread wings flying out of the wreath, upper right"/>
    <ellipse class="falcon falcon-bottom" cx="250" cy="905" rx="150" ry="100" fill="url(#falconTone)"
             role="img" aria-label="Falcon gliding out of the wreath, lower left"/>
  </svg>

  <header class="credits">
    <span class="artist">Velvet Meridian</span>
    <span class="artist">Tomas Reyl</span>
    <span class="title">Hollow Lanterns</span>
  </header>

  <div class="catalogue">0013</div>
  <div class="series">Norreed x Lumenhaus</div>

  <div class="label-mark">Lumenhaus</div>
</main>
</body>
</html>
```